Tarvel Ridge LLC

Need Professional Business cards for New Investment Fund

Target Market(s)

High Quality investors

Industry/Entity Type

Financial

Contact Information for Business Card

Phone Number +1 555 284 6193
Name Pavel Orlinsky
Title Fund Manager
email po@FundTarvel.example
Website www.FundTarvel.example

Colors

Designer to choose colors to be used in the design.

Requirements
Must have
• Must have our Logo and all of the above. Must be made so lettering and loge can be raised

```html
<!DOCTYPE html>
<html lang="en">
<head>
<meta charset="utf-8">
<title>Tarvel Ridge LLC – Business Card</title>
<link rel="stylesheet" href="https://fonts.googleapis.com/css2?family=Source+Serif+4:wght@400;600&display=swap">
<style>
  :root {
    --backdrop: #e9e7e3;
    --card-white: #ffffff;
    --brand-green: #5db22f;
    --ink-dark: #454b44;
    --ink-body: #3d3d3d;
    --on-green: #ffffff;
  }
  * { box-sizing: border-box; margin: 0; padding: 0; }
  html, body {
    width: 1200px;
    height: 1000px;
    overflow: hidden;
    background: var(--backdrop);
    font-family: "Source Serif 4", Georgia, serif;
  }
  .card {
    position: absolute;
    left: 220px;
    width: 760px;
    height: 420px;
    box-shadow: 0 10px 28px rgba(0, 0, 0, 0.18);
  }
  .card-front { top: 70px; background: var(--card-white); }
  .card-back { top: 530px; background: var(--brand-green); }

  .brand-mark {
    position: absolute;
    display: flex;
    align-items: center;
    gap: 14px;
    font-weight: 600;
    letter-spacing: 0.04em;
  }
  .card-front .brand-mark {
    left: 56px;
    top: 186px;
    font-size: 34px;
    color: var(--ink-dark);
  }
  .brand-square {
    width: 22px;
    height: 22px;
    background: currentColor;
  }
  .card-back .brand-mark {
    left: 0;
    right: 0;
    top: 170px;
    justify-content: center;
    font-size: 44px;
    color: var(--on-green);
  }
  .card-back .brand-square { width: 28px; height: 28px; }

  .contact-block {
    position: absolute;
    left: 420px;
    top: 62px;
    color: var(--ink-body);
  }
  .holder-name {
    font-size: 29px;
    font-weight: 400;
    color: var(--brand-green);
    letter-spacing: 0.02em;
    text-transform: uppercase;
    line-height: 1.1;
  }
  .holder-title {
    font-size: 25px;
    color: var(--ink-dark);
    margin-top: 2px;
  }
  .postal-address {
    font-style: normal;
    font-size: 16px;
    line-height: 1.45;
    margin-top: 26px;
  }
  .contact-list {
    list-style: none;
    margin-top: 22px;
  }
  .contact-list li {
    display: flex;
    align-items: center;
    gap: 18px;
    font-size: 17px;
    height: 27px;
  }
  .contact-icon { width: 20px; height: 20px; flex: none; }

  .back-web {
    position: absolute;
    right: 48px;
    bottom: 40px;
    font-size: 20px;
    color: var(--on-green);
    letter-spacing: 0.02em;
  }
</style>
</head>
<body>

<section class="card card-front" aria-label="Business card front">
  <div class="brand-mark"><span class="brand-square"></span>Tarvel Ridge</div>

  <div class="contact-block">
    <h1 class="holder-name">Pavel Orlinsky</h1>
    <p class="holder-title">Fund Manager</p>
    <address class="postal-address">48 Corven Lane, Ashford,<br>CO80412-5530</address>
    <ul class="contact-list">
      <li>
        <svg class="contact-icon" viewBox="0 0 24 24" aria-hidden="true"><path fill="#5db22f" d="M6.6 10.8a15.1 15.1 0 0 0 6.6 6.6l2.2-2.2a1 1 0 0 1 1-.25 11.4 11.4 0 0 0 3.6.6 1 1 0 0 1 1 1V20a1 1 0 0 1-1 1A17 17 0 0 1 3 4a1 1 0 0 1 1-1h3.5a1 1 0 0 1 1 1c0 1.25.2 2.45.6 3.6a1 1 0 0 1-.25 1z"/></svg>
        <span>+1 555 284 6193</span>
      </li>
      <li>
        <svg class="contact-icon" viewBox="0 0 24 24" aria-hidden="true"><rect x="2" y="5" width="20" height="14" fill="#5db22f"/><path d="M2.5 5.5 12 13l9.5-7.5" fill="none" stroke="#fff" stroke-width="1.6"/></svg>
        <span>po@FundTarvel.example</span>
      </li>
      <li>
        <svg class="contact-icon" viewBox="0 0 24 24" aria-hidden="true"><g fill="none" stroke="#5db22f" stroke-width="1.8"><circle cx="12" cy="12" r="9.5"/><ellipse cx="12" cy="12" rx="4.2" ry="9.5"/><path d="M2.5 12h19M4 7h16M4 17h16"/></g></svg>
        <span>www.FundTarvel.example</span>
      </li>
    </ul>
  </div>
</section>

<section class="card card-back" aria-label="Business card back">
  <div class="brand-mark"><span class="brand-square"></span>Tarvel Ridge</div>
  <p class="back-web">www.FundTarvel.example</p>
</section>

</body>
</html>
```